Accountability Project Graphics

I want to create 10 social media graphics (new Instagram size 4:5 (1080 x 1350 pixels) focusing on our Kelmora Accountability App, using any of the 3 pictures attached. Use the attached pics only, NO RANDOM STOCK PHOTOGRAPHY. For the color scheme, use the landing page colors/fonts (attached).
You can add any of the 3 photos attached but I mainly need BOLD text that includes these headlines and sub-headlines on them.
Please NOTE for all the headlines below, also add this sub-headline on each graphic:
Stay Consistent with MB in Your Pocket!
Here are the headlines:
• Stop Starting Over Every Monday
• You don't need more willpower. You need more support
• Built for women who are tired of doing this alone
• When Motivation Fades, MB Checks In
• The Support System You've Been Missing
• Support When Motivation Disappears
• What if MB Checked in Every Day?
• The Missing Piece Isn't Another Diet
• Eat the food you love. Stay accountable every day.
• One Bad Meal Doesn't Mean You Failed
women over 40 trying to lose weight

```html
<!DOCTYPE html>
<html lang="en">
<head>
<meta charset="utf-8">
<title>Kelmora Accountability App – Social Graphics</title>
<link rel="stylesheet" href="https://fonts.googleapis.com/css2?family=Lora:ital,wght@1,600&family=Montserrat:wght@500&display=swap">
<style>
  :root {
    --page-bg: #ffffff;
    --card-edge: #f8d3dd;
    --card-glow: #fdf1f4;
    --headline: #c4416d;
    --subline: #cf4a78;
    --panel-bg: rgba(255, 255, 255, 0.72);
    --avatar-ring: #d6507f;
    --avatar-fill: #b53c63;
    --divider: #e08aa8;
  }
  * { margin: 0; padding: 0; box-sizing: border-box; }
  html, body {
    width: 1200px;
    height: 601px;
    overflow: hidden;
    background: var(--page-bg);
  }
  .graphics-grid {
    position: relative;
    width: 1200px;
    height: 601px;
    display: grid;
    grid-template-columns: repeat(5, 227.5px);
    grid-template-rows: repeat(2, 284px);
    column-gap: 10.6px;
    row-gap: 11px;
    padding: 10px 10.6px;
  }
  .post {
    position: relative;
    overflow: hidden;
    background: radial-gradient(ellipse 70% 60% at 50% 50%, var(--card-glow) 0%, var(--card-edge) 100%);
  }
  .post__headline {
    position: absolute;
    left: 0;
    right: 0;
    top: var(--head-top);
    text-align: center;
    font-family: "Lora", Georgia, serif;
    font-style: italic;
    font-weight: 600;
    font-size: 22px;
    line-height: 25px;
    letter-spacing: -0.4px;
    color: var(--headline);
  }
  .post__subline {
    position: absolute;
    left: 0;
    right: 0;
    top: var(--sub-top);
    text-align: center;
    font-family: "Montserrat", Arial, sans-serif;
    font-weight: 500;
    font-size: 10.2px;
    line-height: 11px;
    letter-spacing: 0.6px;
    color: var(--subline);
  }
  .post__panel {
    position: absolute;
    left: 32.5px;
    top: 37px;
    width: 162px;
    height: 217px;
    border-radius: 14px;
    background: var(--panel-bg);
  }
  .post__avatar {
    position: absolute;
    width: 41px;
    height: 41px;
    border-radius: 50%;
    background: radial-gradient(circle at 50% 60%, var(--avatar-fill) 0%, var(--avatar-ring) 70%);
  }
  .post__divider {
    position: absolute;
    left: 113px;
    width: 1px;
    background: var(--divider);
  }

  .post--stop     { --head-top: 74px; --sub-top: 189px; }
  .post--willpower{ --head-top: 60px; --sub-top: 203px; }
  .post--alone    { --head-top: 60px; --sub-top: 203px; }
  .post--fades    { --head-top: 60px; --sub-top: 216px; }
  .post--missing  { --head-top: 74px; --sub-top: 212px; }
  .post--support  { --head-top: 64px; --sub-top: 198px; }
  .post--everyday { --head-top: 69px; --sub-top: 211px; }
  .post--diet     { --head-top: 69px; --sub-top: 192px; }
  .post--food     { --head-top: 64px; --sub-top: 198px; }
  .post--failed   { --head-top: 64px; --sub-top: 198px; }

  .post--fades .post__avatar    { left: 19.5px; top: 24.5px; }
  .post--everyday .post__avatar { left: 20px;   top: 25px; }
  .post--fades .post__divider    { top: 173px; height: 30px; }
  .post--everyday .post__divider { top: 165px; height: 29px; }
</style>
</head>
<body>
<main class="graphics-grid">

  <article class="post post--stop">
    <h2 class="post__headline">Stop Starting<br>over every<br>Monday</h2>
    <p class="post__subline">Stay Consistent with<br>MB in Your Pocket!</p>
  </article>

  <article class="post post--willpower">
    <h2 class="post__headline">You don’t need<br>more willpower.<br>You need more<br>support.</h2>
    <p class="post__subline">Stay Consistent with<br>MB in Your Pocket!</p>
  </article>

  <article class="post post--alone">
    <h2 class="post__headline">Built for<br>women who are<br>tired of doing<br>this alone</h2>
    <p class="post__subline">Stay Consistent with<br>MB in Your Pocket!</p>
  </article>

  <article class="post post--fades">
    <div class="post__panel"></div>
    <div class="post__avatar" role="img" aria-label="Circular portrait photo of MB, the accountability coach"></div>
    <h2 class="post__headline">When<br>motivation<br>fades<br>MB Check in</h2>
    <div class="post__divider"></div>
    <p class="post__subline">Stay Consistent with<br>MB in Your Pocket!</p>
  </article>

  <article class="post post--missing">
    <h2 class="post__headline">The support<br>system you’ve<br>been missing</h2>
    <p class="post__subline">Stay Consistent with<br>MB in Your Pocket!</p>
  </article>

  <article class="post post--support">
    <h2 class="post__headline">Support<br>when<br>motivation<br>disappears</h2>
    <p class="post__subline">Stay Consistent with<br>MB in Your Pocket!</p>
  </article>

  <article class="post post--everyday">
    <div class="post__panel"></div>
    <div class="post__avatar" role="img" aria-label="Circular portrait photo of MB, the accountability coach"></div>
    <h2 class="post__headline">What if<br>MB checks in<br>everyday?</h2>
    <div class="post__divider"></div>
    <p class="post__subline">Stay Consistent with<br>MB in Your Pocket!</p>
  </article>

  <article class="post post--diet">
    <h2 class="post__headline">The Missing<br>piece isn’t<br>another diet</h2>
    <p class="post__subline">Stay Consistent with<br>MB in Your Pocket!</p>
  </article>

  <article class="post post--food">
    <h2 class="post__headline">Eat the food<br>you love. Stay<br>accountable<br>everyday</h2>
    <p class="post__subline">Stay Consistent with<br>MB in Your Pocket!</p>
  </article>

  <article class="post post--failed">
    <h2 class="post__headline">One bad<br>meal doesn’t<br>mean you<br>failed</h2>
    <p class="post__subline">Stay Consistent with<br>MB in Your Pocket!</p>
  </article>

</main>
</body>
</html>
```